依頼概要
■依頼の目的/概要
弊社(森岡緑耕苑)が販売予定している「もちぽろ玉」(お菓子)のラベルデザインをお願いします。米粉100%のお菓子です。

■依頼詳細
添付写真を参考にしてください。パッケージは白とクラフトの両方を用意しています。デザインによってどちらかに決定します。パッケージは白、クラフト共に縦、横どちらも15㎝です。(端から端まで)真ん中から下が透明になっていて、中身が見えます。

私たちの農園は自然農法という無肥料・無農薬・自家採種でのこだわりの栽培方法で野菜・お米・穀物等を作っています。信条は「土がきれいになれば世界が平和になる」です。

今回使っている材料は弊社の自然農法のお米100%にフィリピン産の自然農法の黒糖をまぶしてあります。原材料はお米と黒糖だけで、添加物等も一切使っていません。しかも化学肥料や農薬等を使わない自然農法産ですので、アレルギーのある子どもでも安心して食べて頂けます。

「もちぽろ玉」は、アルファー化(糊化)米粉を作る過程で出来る玉状のお米100%のお菓子(おやつのポルンの製造で使っている機械の改良版)ですが、おかきのように硬くはなく、食感が柔らかで少しもっちりとしていて、食べ始めると止まらなくなります。まぶしてある砂糖は普通の砂糖とは違って、黒糖を使っていますので、これまた風味があって止まりません。内容量は40gと少な目の食べ切りサイズになります。アルファー化米粉は、グルテンの代わりになるもので、これを米粉に少し配合すると米粉100%のパンが焼けるというものです。このパフはアルファー化米粉100%で出来ていますので、少しもっちりしっとりしています。

■その他要望
多くの方に手軽に手に取って食べて頂けるお菓子になればいいなと思います。
弊社のロゴマークをデザインの中に入れて頂きたいです。
ロゴマークも添付してあります。(ロゴマークは4種類の形式で添付しています)
ロゴのグリーン部分の色はC70 M40 Y85 K35です。
イラストレータのバージョンはcs6になります。
その他何かご不明な点がございましたら、お気軽にご質問下さい。
よろしくお願いいたします。
ラベルは、シール式で張り付けるようにします。
情報が不足しておりました。
表記に関してですが、
「自然農法」「無農薬」「無肥料」という言葉は使えません。
「自然農法」→「肥料や農薬を使わない栽培法」
「無農薬」→「農薬不使用」
「無肥料」→「肥料不使用」
となります。
尚、今回の商品にかんしては「自家採種」という言葉は使いません。
商品の単価はそれほど高くありませんので、
シンプルでラベルシールの大きさもほどほどに抑えたいと思っております。
何卒よろしくお願いいたします。
■ 選んだ理由

お菓子のラベルらしいデザインでした。
クレヨンでの手書きの輪がとても温かみがあり親しみやすいデザインになっていて気に入りました。分かりやすくシンプルで色合いも良く多くの方にこの商品を手に取って頂けそうに思いました。ありがとうございました。

■ 提案者全員のお礼・コメント

多くのデザイナーさんにご提案頂き感謝申し上げます。
また機会がありましたら、どうぞよろしくお願いいたします。

```html
<!DOCTYPE html>
<html lang="ja">
<head>
<meta charset="UTF-8">
<title>もちぽろ玉 ラベル</title>
<link rel="stylesheet" href="https://fonts.googleapis.com/css2?family=Dela+Gothic+One&family=M+PLUS+Rounded+1c:wght@500;800&display=swap">
<style>
  :root {
    --page-bg: #f2f1ee;
    --label-bg: #ffffff;
    --ink: #141414;
    --leaf: #3f6a2c;
    --leaf-soft: #5a8a3c;
    --muted: #4a4a4a;
  }
  html, body {
    margin: 0;
    padding: 0;
    width: 846px;
    height: 1200px;
    overflow: hidden;
    background: var(--page-bg);
  }
  .canvas {
    position: relative;
    width: 846px;
    height: 1200px;
  }
  .label {
    position: absolute;
    left: 98px;
    top: 250px;
    width: 650px;
    height: 650px;
    background: var(--label-bg);
    box-shadow: 0 2px 10px rgba(0,0,0,0.08);
    font-family: "M PLUS Rounded 1c", sans-serif;
    color: var(--ink);
  }
  .title-top,
  .title-bottom {
    position: absolute;
    font-family: "Dela Gothic One", sans-serif;
    line-height: 1;
    color: var(--ink);
    letter-spacing: -4px;
  }
  .title-top {
    left: 48px;
    top: 40px;
    font-size: 190px;
  }
  .title-bottom {
    left: 60px;
    top: 380px;
    font-size: 200px;
  }
  .title-badge {
    position: absolute;
    left: 300px;
    top: 240px;
    width: 150px;
    height: 150px;
    border-radius: 50%;
    background: var(--leaf-soft);
    color: #fff;
    font-family: "Dela Gothic One", sans-serif;
    font-size: 64px;
    display: flex;
    align-items: center;
    justify-content: center;
    letter-spacing: -2px;
  }
  .claim {
    position: absolute;
    left: 58px;
    top: 270px;
    font-size: 26px;
    font-weight: 800;
    line-height: 1.35;
    color: var(--muted);
  }
  .ingredient {
    position: absolute;
    right: 48px;
    top: 280px;
    font-size: 26px;
    font-weight: 800;
    color: var(--muted);
  }
  .brand {
    position: absolute;
    left: 48px;
    bottom: 36px;
    display: flex;
    align-items: center;
    gap: 12px;
  }
  .brand-dot {
    width: 30px;
    height: 30px;
    border-radius: 50%;
    background: var(--leaf);
  }
  .brand-name {
    font-family: "M PLUS Rounded 1c", sans-serif;
    font-weight: 800;
    font-size: 36px;
    color: var(--leaf);
    letter-spacing: 3px;
  }
</style>
</head>
<body>
  <div class="canvas">
    <section class="label">
      <div class="title-top">もち</div>
      <div class="title-badge">ぽろ</div>
      <div class="title-bottom">玉</div>
      <p class="claim" style="margin:0">農薬・肥料<br>不使用</p>
      <p class="ingredient" style="margin:0">米粉100%</p>
      <div class="brand">
        <span class="brand-dot"></span>
        <span class="brand-name">MIDORI</span>
      </div>
    </section>
  </div>
</body>
</html>
```